Tampa, Florida based Real Estate company Business Cards

Need ideas for real estate business cards
Updates

Need extra days to review

Industry/Entity Type

Real Estate

Contact Information for Business Card

Space for image, space for logo, contact information space

Font styles to use
Sans Serif

Colors

Designer to choose colors to be used in the design.

Requirements
Must have
• Options to have duplicate content on the back of card for a team of agents.

```html
<!DOCTYPE html>
<html lang="en">
<head>
<meta charset="utf-8">
<title>Harborline Homes Business Cards</title>
<link href="https://fonts.googleapis.com/css2?family=Roboto:wght@400;500;700&display=swap" rel="stylesheet">
<style>
  :root {
    --bg: #d8d8d8;
    --card: #ffffff;
    --navy: #1a1649;
    --accent: #f2374f;
    --line-grey: #d9d9d9;
    --text-light: #ffffff;
  }
  * { margin: 0; padding: 0; box-sizing: border-box; }
  html, body {
    width: 1200px; height: 900px; overflow: hidden;
    background: var(--bg);
    font-family: 'Roboto', sans-serif;
  }
  .card {
    position: absolute;
    background: var(--card);
    box-shadow: 0 6px 18px rgba(0,0,0,0.35);
    overflow: hidden;
  }
  .card--front { left: 240px; top: 47px; width: 676px; height: 387px; }
  .card--back  { left: 238px; top: 467px; width: 681px; height: 388px; }

  .brand {
    position: absolute;
    display: flex; align-items: center;
    color: var(--navy);
    font-weight: 700;
    white-space: nowrap;
  }
  .brand__dot {
    border-radius: 50%;
    background: var(--navy);
    flex: none;
  }
  .card--front .brand {
    left: 0; right: 0; top: 0; bottom: 0;
    justify-content: center;
    gap: 16px;
    font-size: 46px;
    letter-spacing: 4px;
  }
  .card--front .brand__dot { width: 30px; height: 30px; }

  .card--back .brand {
    left: 168px; top: 194px;
    gap: 12px;
    font-size: 22px;
    letter-spacing: 2px;
    transform: translate(-50%, -50%) rotate(-90deg);
  }
  .card--back .brand__dot { width: 18px; height: 18px; }

  .panel-shape { position: absolute; left: 0; top: 0; }

  .agent {
    position: absolute; left: 370px; top: 30px;
    color: var(--text-light);
  }
  .agent__name { font-size: 32px; font-weight: 700; line-height: 1.15; }
  .agent__role { font-size: 26px; font-weight: 500; color: var(--accent); line-height: 1.2; }

  .contact-list {
    position: absolute; left: 355px; top: 140px;
    list-style: none;
    color: var(--text-light);
    font-size: 16px;
    line-height: 1.25;
  }
  .contact-list li {
    display: flex; align-items: center; gap: 10px;
    height: 31px; margin-bottom: 16px;
  }
  .contact-list li.contact--address { margin-bottom: 22px; }
  .contact-icon {
    width: 31px; height: 31px; border-radius: 50%;
    background: #ffffff; flex: none;
    display: flex; align-items: center; justify-content: center;
  }
  .contact-icon svg { width: 18px; height: 18px; }
</style>
</head>
<body>

<section class="card card--front">
  <div class="brand"><span class="brand__dot"></span>HARBORLINE HOMES</div>
</section>

<section class="card card--back">
  <svg class="panel-shape" width="681" height="388" viewBox="0 0 681 388">
    <path d="M358 0 Q318 194 360 388" fill="none" stroke="var(--line-grey)" stroke-width="14"/>
    <path d="M340 0 Q300 194 342 388" fill="none" stroke="var(--line-grey)" stroke-width="2"/>
    <path d="M350 0 H681 V388 H353 Q311 194 350 0 Z" fill="var(--navy)"/>
  </svg>

  <div class="brand"><span class="brand__dot"></span>HARBORLINE HOMES</div>

  <div class="agent">
    <div class="agent__name">Marek Dolan</div>
    <div class="agent__role">Agent</div>
  </div>

  <ul class="contact-list">
    <li class="contact--address">
      <span class="contact-icon">
        <svg viewBox="0 0 24 24" fill="none" stroke="var(--navy)" stroke-width="2"><path d="M12 22s7-7 7-12a7 7 0 0 0-14 0c0 5 7 12 7 12z"/><circle cx="12" cy="10" r="2.5"/></svg>
      </span>
      <span>St,7 #4127, Near Bayview Plaza<br>Sector 14C</span>
    </li>
    <li>
      <span class="contact-icon">
        <svg viewBox="0 0 24 24" fill="none" stroke="var(--navy)" stroke-width="2"><path d="M5 3h4l2 5-3 2a11 11 0 0 0 6 6l2-3 5 2v4a2 2 0 0 1-2 2A17 17 0 0 1 3 5a2 2 0 0 1 2-2z"/></svg>
      </span>
      <span>555.014.2738</span>
    </li>
    <li>
      <span class="contact-icon">
        <svg viewBox="0 0 24 24" fill="none" stroke="var(--navy)" stroke-width="2"><rect x="3" y="6" width="18" height="12" rx="1"/><path d="M3 7l9 6 9-6"/></svg>
      </span>
      <span>info@harborlinehomes.com</span>
    </li>
    <li>
      <span class="contact-icon">
        <svg viewBox="0 0 24 24" fill="none" stroke="var(--navy)" stroke-width="2"><circle cx="12" cy="12" r="9"/><path d="M3 12h18M12 3c3 3 3 15 0 18M12 3c-3 3-3 15 0 18"/></svg>
      </span>
      <span>www.harborlinehomes.com</span>
    </li>
  </ul>
</section>

</body>
</html>
```